Housecleaning advertisement

We are a professional residential housecleaning service, in business since 2005, providing detailed, eco-friendly housecleaning to our clients. We are looking for a design that can be used in monthly coupon books ( 4c), quarterly local magazine (biz card sized 4c) and weekly newspaper ad (biz card sized b/w). We are looking for a retro feel - think 1940s kitchens - yellow, turquoise, bright red. we want to stress that we are a local firm, not a one-size fits all franchise. We provide very personalized service (linen changes, pet-friendly, flexible scheduling, sit down with customer prior to initial cleaning and discuss their priorities so that we know what they are looking for and deliver 110% each and every clean to them - and a a very reasonable price.) Our logo is a red car with two cleaners in it. Text for the ad :
Relax and enjoy your sparkling, clean, ready-for-company home!
Test drive our detailed, eco-friendly housecleaning
four hours for $100 (new clients only)
some bulleted points
* 100% Woman-owned and staffed. We know how to clean and tidy up - and treat your home with care and respect.
* Eco-friendly products - healthier for you and your family
* Fully insured and bonded.
415.382.9156
www.tidywrenhaus.net
Target Market(s)
Professional women ages 30-65 in the New Haven County, Ct market
Industry/Entity Type
Residential
Requirements
Nice to have
- retro 1940s 1950s

```html
<!DOCTYPE html>
<html lang="en">
<head>
<meta charset="utf-8">
<title>Tidy Wren Haus Cleaning – Coupon Ad</title>
<link rel="stylesheet" href="https://fonts.googleapis.com/css2?family=Bebas+Neue&family=Lobster&family=Oswald:wght@300;400;500&display=swap">
<style>
  :root {
    --frame: #f7ef9c;
    --frame-edge: #f3c6d8;
    --teal: #7fd6de;
    --teal-light: #a9e6ea;
    --teal-deep: #5ec8d2;
    --white: #ffffff;
    --orange: #f7a65a;
    --cream: #fff6dc;
    --car-red: #e8404d;
    --car-sky: #c9eef1;
  }
  * { margin: 0; padding: 0; box-sizing: border-box; }
  html, body { width: 1200px; height: 686px; overflow: hidden; background: var(--frame); }
  .ad {
    position: relative;
    width: 1200px; height: 686px;
    background: var(--frame);
    border: 4px solid var(--frame-edge);
    font-family: "Oswald", sans-serif;
    color: var(--white);
  }
  .panel {
    position: absolute;
    left: 23px; top: 14px; width: 1154px; height: 655px;
    background: radial-gradient(ellipse at 45% 45%, var(--teal-light) 0%, var(--teal) 55%, var(--teal-deep) 100%);
    box-shadow: 0 2px 6px rgba(0,0,0,0.25);
  }
  .panel::before {
    content: ""; position: absolute; inset: 8px;
    border: 2px dashed rgba(255,255,255,0.55);
  }
  .rule-h { position: absolute; border-top: 2px dotted rgba(255,255,255,0.75); }
  .rule-v { position: absolute; border-left: 2px dotted rgba(255,255,255,0.75); }
  .business-name {
    position: absolute; left: 62px; top: 26px;
    font-family: "Bebas Neue", sans-serif; font-size: 78px; line-height: 1;
    letter-spacing: 1px; white-space: nowrap;
  }
  .contact { position: absolute; left: 858px; top: 30px; font-family: "Bebas Neue", sans-serif; line-height: 1; }
  .contact .web { font-size: 26px; letter-spacing: 0.5px; }
  .contact .phone { font-size: 52px; margin-top: 2px; letter-spacing: 0.5px; }
  .headline {
    position: absolute; left: 0; top: 128px; width: 1154px;
    text-align: center; font-family: "Lobster", cursive;
    font-size: 66px; line-height: 74px; color: var(--orange);
    -webkit-text-stroke: 2px var(--cream); paint-order: stroke fill;
    text-shadow: 0 0 3px var(--cream), 2px 2px 0 var(--cream);
  }
  .benefit { position: absolute; left: 40px; width: 620px; text-align: center; }
  .benefit h2 { font-weight: 500; font-size: 37px; line-height: 1.1; letter-spacing: 0.3px; }
  .benefit p { font-weight: 300; font-size: 22px; line-height: 1.4; }
  .logo-art {
    position: absolute; left: 700px; top: 320px; width: 430px; height: 245px;
    border-radius: 40% 40% 30% 30%;
    background: radial-gradient(ellipse at 50% 60%, var(--car-red) 0%, #f07a6e 38%, var(--car-sky) 70%, transparent 72%);
  }
  .offer { position: absolute; left: 700px; top: 565px; width: 430px; text-align: center; font-weight: 400; }
  .offer h3 { font-weight: 500; font-size: 23px; line-height: 1.1; }
  .offer p { font-size: 16px; margin-top: 6px; }
</style>
</head>
<body>
<div class="ad">
  <div class="panel">
    <h1 class="business-name">Tidy Wren Haus Cleaning</h1>
    <div class="rule-v" style="left:838px; top:30px; height:80px;"></div>
    <div class="contact">
      <div class="web">www.tidywrenhaus.net</div>
      <div class="phone">415.382.9156</div>
    </div>
    <div class="rule-h" style="left:55px; top:119px; width:1045px;"></div>

    <p class="headline">Relax and enjoy your sparkling,<br>clean, ready-for-company home!</p>

    <div class="rule-h" style="left:55px; top:292px; width:1045px;"></div>
    <div class="rule-v" style="left:683px; top:310px; height:320px;"></div>

    <div class="benefit" style="top:310px;">
      <h2>* 100% Woman-owned and staffed.</h2>
      <p>We know how to clean and tidy up and<br>treat your home with care and respect.</p>
    </div>
    <div class="rule-h" style="left:120px; top:443px; width:460px;"></div>
    <div class="benefit" style="top:457px;">
      <h2>* Eco-friendly products.</h2>
      <p>healthier for you and your family</p>
    </div>
    <div class="rule-h" style="left:120px; top:538px; width:460px;"></div>
    <div class="benefit" style="top:570px;">
      <h2>* Fully insured and bonded.</h2>
    </div>

    <div class="logo-art" role="img" aria-label="Illustrated logo: red convertible car carrying two cleaners with mop and broom"></div>
    <div class="offer">
      <h3>Test drive our detailed,<br>eco-friendly housecleaning</h3>
      <p>Four hours for $100 (new clients only)</p>
    </div>
  </div>
</div>
</body>
</html>
```